Research and Development Technical Training for Process Engineering

We are creating a TeamPoint site that will contain links to several training materials. I will create and upload the content, just looking for graphics and a basic layout for a single homepage. The page should contain unique graphics for the following topics/categories: Methodology, Equipment Training, Design References, Safety & Environmental, and Technology. (See attached example. Layout example DOES NOT need to be followed, only an example).
Also, a graphic to be used for a Powerpoint template that is cohesive with the graphics previously mentioned. Space for a company logo required. Professional/business application. Company logo already exists, it is blue and red but these colors are not required to be used as a theme.
Industry/Entity Type
Training
Number of Pages Required
1 page
Colors
Designer to choose colors to be used in the design.
Look and feel
Each slider illustrates characteristics of the customer's brand and the style your logo design should communicate.

```html
<!DOCTYPE html>
<html lang="en">
<head>
<meta charset="utf-8">
<title>Verlane — Research &amp; Development Technical Training</title>
<link href="https://fonts.googleapis.com/css2?family=Lato:wght@400;700;900&display=swap" rel="stylesheet">
<style>
  :root {
    --sky: #1ab0ea;
    --wave-blue: #5bc2ef;
    --wave-pink: #f9c6cc;
    --wave-pink-soft: #f2dadc;
    --ink: #222222;
    --text: #444444;
    --paper: #ffffff;
    --header-bg: #eef8fd;
    --section-gray: #efefef;
    --footer-bg: #333333;
    --slate: #58536a;
    --mint: #6cc6a6;
    --teal: #0fcfd0;
    --coral: #f25f5c;
    --umber: #3b2219;
    --brand-red: #d42a2f;
  }
  * { margin: 0; padding: 0; box-sizing: border-box; }
  html, body { width: 1200px; height: 2601px; overflow: hidden; }
  body {
    position: relative;
    background: var(--paper);
    font-family: "Lato", Arial, sans-serif;
    color: var(--text);
  }
  .abs { position: absolute; }

  /* Header */
  .site-header {
    position: absolute; left: 0; top: 0; width: 1200px; height: 160px;
    background: linear-gradient(180deg, #f5fbfe, var(--header-bg));
  }
  .main-nav { position: absolute; top: 36px; left: 0; width: 100%; }
  .main-nav a {
    position: absolute; font-size: 16px; font-weight: 700; color: var(--ink);
    text-decoration: none; letter-spacing: 0.3px;
  }
  .brand {
    position: absolute; left: 878px; top: 22px; height: 50px;
    display: flex; align-items: center; gap: 12px;
  }
  .brand-dot { width: 46px; height: 46px; border-radius: 50%; background: var(--sky); }
  .brand-name { font-size: 30px; font-weight: 900; color: var(--brand-red); letter-spacing: 0.5px; }

  /* Hero */
  .hero-art { position: absolute; left: 0; top: 0; }
  .hero-copy { position: absolute; left: 99px; top: 252px; color: var(--paper); }
  .hero-title { font-size: 40px; font-weight: 900; letter-spacing: 0.5px; line-height: 1.1; }
  .hero-subtitle { font-size: 33px; font-weight: 700; margin-top: 18px; line-height: 1.1; }
  .hero-text { font-size: 17px; font-weight: 700; line-height: 25px; margin-top: 20px; width: 480px; }
  .btn-outline {
    display: inline-block; border: 2px solid var(--paper); color: var(--paper);
    font-size: 16px; font-weight: 700; text-decoration: none;
  }
  .hero-btn { position: absolute; left: 99px; top: 458px; width: 121px; height: 51px; line-height: 47px; text-align: center; }

  /* Intro */
  .intro { position: absolute; left: 0; top: 760px; width: 1200px; text-align: center; }
  .intro-title { font-size: 33px; font-weight: 700; color: var(--sky); letter-spacing: 0.3px; }
  .intro-rule { width: 80px; height: 3px; background: var(--sky); margin: 14px auto 0; }
  .intro-text { width: 980px; margin: 40px auto 0; font-size: 14px; line-height: 24px; color: var(--text); }
  .intro-text + .intro-text { margin-top: 10px; }
  .btn-pill {
    position: absolute; left: 538px; top: 1046px; width: 124px; height: 44px; line-height: 44px;
    border-radius: 22px; background: var(--sky); color: var(--paper); font-size: 16px; font-weight: 700;
    text-align: center; text-decoration: none;
  }

  /* Topic tiles */
  .topics { position: absolute; left: 0; top: 1158px; width: 1200px; height: 980px; background: var(--section-gray); overflow: hidden; }
  .tile { position: absolute; }
  .tile svg { position: absolute; left: 0; top: 0; width: 100%; height: 100%; }
  .tile-art { position: absolute; border-radius: 16px; }
  .tile-featured-copy { position: absolute; left: 309px; top: 212px; width: 582px; text-align: center; color: var(--paper); }
  .tile-title { font-size: 27px; font-weight: 900; letter-spacing: 0.3px; }
  .tile-text { width: 480px; margin: 14px auto 0; font-size: 15px; line-height: 24px; }
  .tile-btn { margin-top: 22px; width: 124px; height: 45px; line-height: 41px; border-radius: 23px; font-size: 16px; }

  /* Footer */
  .footer-art { position: absolute; left: 0; top: 2100px; }
  .footer-brand {
    position: absolute; left: 0; top: 2314px; width: 1200px;
    display: flex; justify-content: center; align-items: center; gap: 12px;
  }
  .footer-brand .brand-dot { width: 62px; height: 62px; background: var(--paper); }
  .footer-brand .brand-name { color: var(--paper); font-size: 32px; }
  .footer-nav {
    position: absolute; left: 0; top: 2442px; width: 1200px;
    display: flex; justify-content: center; align-items: center; gap: 38px;
    font-size: 18px; font-weight: 700; color: var(--paper);
  }
  .footer-nav a { color: var(--paper); text-decoration: none; }
  .footer-rule { position: absolute; left: 99px; top: 2514px; width: 1002px; height: 2px; background: #d0d0d0; }
  .copyright { position: absolute; left: 0; top: 2548px; width: 1200px; text-align: center; font-size: 17px; font-weight: 700; color: var(--paper); }
</style>
</head>
<body>

  <header class="site-header">
    <nav class="main-nav">
      <a style="left:99px" href="#">HOME</a>
      <a style="left:199px" href="#">ABOUT US</a>
      <a style="left:327px" href="#">TECHNOLOGY</a>
      <a style="left:487px" href="#">TRAINING</a>
      <a style="left:615px" href="#">BLOG</a>
      <a style="left:712px" href="#">CONTACT</a>
    </nav>
    <div class="brand">
      <span class="brand-dot"></span>
      <span class="brand-name">VERLANE</span>
    </div>
  </header>

  <svg class="hero-art" width="1200" height="720" viewBox="0 0 1200 720">
    <defs>
      <linearGradient id="heroGlow" x1="0" y1="0" x2="1" y2="0.4">
        <stop offset="0" stop-color="#0b1426"/>
        <stop offset="0.45" stop-color="#10213f"/>
        <stop offset="0.75" stop-color="#1d4f8a"/>
        <stop offset="1" stop-color="#2a77b8"/>
      </linearGradient>
    </defs>
    <path d="M0,600 L0,680 C200,640 380,705 600,672 C850,640 1000,712 1200,702 L1200,590 Z" fill="var(--wave-pink)"/>
    <path d="M0,100 C250,70 450,118 700,92 C900,72 1050,105 1200,82 L1200,650 C1000,668 850,616 650,645 C400,675 200,612 0,642 Z" fill="var(--wave-blue)"/>
    <path role="img" aria-label="Digital hand touching a glowing network of technology icons" d="M0,132 C250,95 450,140 700,118 C900,98 1050,132 1200,112 L1200,606 C1000,632 850,585 650,614 C400,648 200,585 0,614 Z" fill="url(#heroGlow)"/>
  </svg>

  <div class="hero-copy">
    <h1 class="hero-title">RESEARCH &amp; DEVELOPMENT</h1>
    <h2 class="hero-subtitle">TECHNICAL TRAINING</h2>
    <p class="hero-text">Duis aute irure dolor in reprehenderit in voluptate velit esse cillum dolore eu fugiat nulla pariatur.</p>
  </div>
  <a class="btn-outline hero-btn" href="#">READ MORE</a>

  <section class="intro">
    <h2 class="intro-title">OUR TEAMPOINT TECHNOLOGY</h2>
    <div class="intro-rule"></div>
    <p class="intro-text">Nemo enim ipsam voluptatem quia voluptas sit aspernatur aut odit aut fugit, sed quia consequuntur magni dolores eos qui ratione voluptatem sequi nesciunt. Neque porro quisquam est, qui dolorem ipsum quia dolor sit amet, consectetur, adipisci velit, sed quia non numquam eius modi tempora incidunt ut labore et dolore magnam aliquam quaerat voluptatem.</p>
    <p class="intro-text">Ut enim ad minima veniam, quis nostrum exercitationem ullam corporis suscipit laboriosam, nisi ut aliquid ex ea commodi consequatur. Quis autem vel eum iure repre henderit qui in ea voluptate velit esse quam nihil molestiae consequatur,.</p>
  </section>
  <a class="btn-pill" href="#">READ MORE</a>

  <section class="topics">
    <!-- Methodology -->
    <div class="tile" style="left:-35px; top:96px; width:434px; height:420px;">
      <svg viewBox="0 0 200 100" preserveAspectRatio="none"><path d="M18,41 L86,7 Q100,0 114,7 L182,41 Q200,50 182,59 L114,93 Q100,100 86,93 L18,59 Q0,50 18,41 Z" fill="var(--slate)"/></svg>
      <div class="tile-art" role="img" aria-label="Methodology illustration: laptop, coffee and notes on a desk" style="left:75px; top:110px; width:230px; height:200px; background:linear-gradient(135deg,#8a8f98,#6b6f79);"></div>
    </div>
    <!-- Design References -->
    <div class="tile" style="left:812px; top:96px; width:456px; height:420px;">
      <svg viewBox="0 0 200 100" preserveAspectRatio="none"><path d="M18,41 L86,7 Q100,0 114,7 L182,41 Q200,50 182,59 L114,93 Q100,100 86,93 L18,59 Q0,50 18,41 Z" fill="var(--mint)"/></svg>
      <div class="tile-art" role="img" aria-label="Design references illustration: monitor with charts, checklist and scroll" style="left:118px; top:120px; width:240px; height:190px; background:linear-gradient(135deg,#3f4a57,#c0394a);"></div>
    </div>
    <!-- Safety & Environmental -->
    <div class="tile" style="left:95px; top:455px; width:503px; height:421px;">
      <svg viewBox="0 0 200 100" preserveAspectRatio="none"><path d="M18,41 L86,7 Q100,0 114,7 L182,41 Q200,50 182,59 L114,93 Q100,100 86,93 L18,59 Q0,50 18,41 Z" fill="var(--teal)"/></svg>
      <div class="tile-art" role="img" aria-label="Safety and environmental illustration: umbrella sheltering a laptop with a shield" style="left:140px; top:105px; width:220px; height:210px; border-radius:50%; background:radial-gradient(circle,#3fa9a8,#10b7b8);"></div>
    </div>
    <!-- Technology -->
    <div class="tile" style="left:520px; top:455px; width:586px; height:421px;">
      <svg viewBox="0 0 200 100" preserveAspectRatio="none"><path d="M18,41 L86,7 Q100,0 114,7 L182,41 Q200,50 182,59 L114,93 Q100,100 86,93 L18,59 Q0,50 18,41 Z" fill="var(--coral)"/></svg>
      <div class="tile-art" role="img" aria-label="Technology illustration: monitor with growth chart, target and cloud" style="left:190px; top:110px; width:240px; height:200px; background:linear-gradient(135deg,#283c5a,#f2c230);"></div>
    </div>
    <!-- Equipment (featured) -->
    <div class="tile" style="left:304px; top:92px; width:592px; height:428px;">
      <svg viewBox="0 0 200 100" preserveAspectRatio="none"><path d="M18,41 L86,7 Q100,0 114,7 L182,41 Q200,50 182,59 L114,93 Q100,100 86,93 L18,59 Q0,50 18,41 Z" fill="var(--umber)" stroke="#1e100b" stroke-width="3" vector-effect="non-scaling-stroke"/></svg>
      <svg viewBox="0 0 200 100" preserveAspectRatio="none" style="left:10px; top:8px; width:572px; height:412px;"><path d="M18,41 L86,7 Q100,0 114,7 L182,41 Q200,50 182,59 L114,93 Q100,100 86,93 L18,59 Q0,50 18,41 Z" fill="none" stroke="#f4e9e4" stroke-width="2" vector-effect="non-scaling-stroke"/></svg>
    </div>
    <div class="tile-featured-copy" style="left:309px; top:218px;">
      <h3 class="tile-title">EQUIPMENT</h3>
      <p class="tile-text">Nemo enim ipsam voluptatem quia voluptas sit aspernatur aut odit aut fugit, sed quia con sequuntur magni dolores.</p>
      <a class="btn-outline tile-btn" href="#">READ MORE</a>
    </div>
  </section>

  <svg class="footer-art" width="1200" height="501" viewBox="0 0 1200 501">
    <path d="M0,20 C200,0 400,60 650,30 C900,0 1050,40 1200,15 L1200,130 L0,130 Z" fill="var(--wave-pink-soft)"/>
    <path d="M0,120 C200,75 380,140 620,100 C850,65 1000,125 1200,95 L1200,200 L0,200 Z" fill="var(--wave-blue)"/>
    <path d="M0,130 C230,95 420,150 660,112 C880,82 1040,140 1200,120 L1200,501 L0,501 Z" fill="var(--footer-bg)"/>
  </svg>

  <footer>
    <div class="footer-brand">
      <span class="brand-dot"></span>
      <span class="brand-name">VERLANE</span>
    </div>
    <nav class="footer-nav">
      <a href="#">HOME</a><span>I</span>
      <a href="#">ABOUT US</a><span>I</span>
      <a href="#">TECHNOLOGY</a><span>I</span>
      <a href="#">TRAINING</a><span>I</span>
      <a href="#">BLOG</a><span>I</span>
      <a href="#">CONTACT</a>
    </nav>
    <div class="footer-rule"></div>
    <p class="copyright">Copyrights @ 2018 Verlane. All Rights Reserved.</p>
  </footer>

</body>
</html>
```